Park furniture company needs a new product flyer

We're a street and park furniture supply company and we have a new range of furniture that we would like to showcase to prospective customers.
Pictures, logo and copy attached.
Furniture pictures are also available with a black background.
Warranty information needs to feature on the flyer.
Recycled content information needs to feature on the flyer.

Target Market(s)

Landscape Architects

Font styles to use
Serif

Requirements
Must have
• Professional fonts and graphics.
Should not have
• comic sans or similar fonts - cheap graphics

```html
<!DOCTYPE html>
<html lang="en">
<head>
<meta charset="utf-8">
<title>Avenue Commons – Product Flyer</title>
<link href="https://fonts.googleapis.com/css2?family=Montserrat:wght@400;600;700&display=swap" rel="stylesheet">
<style>
  :root {
    --paper: #ffffff;
    --sky: #dbe3f3;
    --brand-blue: #0a73bb;
    --slate: #555656;
    --ink-dark: #4a4a4c;
    --white: #ffffff;
    --timber: #b0592a;
    --timber-deep: #7a3a1a;
    --charcoal-slat: #5a5550;
    --frame: #c9c0ae;
  }
  * { box-sizing: border-box; margin: 0; padding: 0; }
  html, body { width: 849px; height: 1200px; overflow: hidden; background: var(--paper); }
  body { font-family: "Montserrat", Arial, sans-serif; position: relative; }

  .flyer { position: relative; width: 849px; height: 1200px; background: var(--paper); }

  .panel-gallery { position: absolute; left: 40px; top: 161px; width: 377px; height: 719px; background: var(--sky); }
  .panel-copy { position: absolute; left: 417px; top: 161px; width: 376px; height: 719px; background: var(--brand-blue); color: var(--white); padding: 28px 16px 0 28px; }

  .brand { position: absolute; right: 56px; top: 46px; text-align: right; color: var(--ink-dark); font-weight: 700; }
  .brand-name { font-size: 64px; line-height: 1; letter-spacing: 1px; }
  .brand-line { font-size: 28px; line-height: 1.1; margin-top: 4px; }

  .product-shot { position: absolute; border-radius: 4px; }
  .shot-seat { left: 70px; top: 22px; width: 300px; height: 386px; background: linear-gradient(160deg, var(--timber) 0%, var(--timber-deep) 60%, var(--frame) 100%); }
  .shot-table { left: 98px; top: 438px; width: 268px; height: 120px; background: linear-gradient(180deg, var(--charcoal-slat) 0%, var(--frame) 100%); }
  .shot-setting { left: 118px; top: 540px; width: 258px; height: 200px; background: linear-gradient(170deg, var(--charcoal-slat) 0%, var(--frame) 100%); }
  .shot-bench { left: 108px; top: 750px; width: 242px; height: 118px; background: linear-gradient(180deg, var(--timber) 0%, var(--timber-deep) 55%, var(--frame) 100%); }

  .lead { font-size: 19px; font-weight: 700; line-height: 29.5px; letter-spacing: 0.6px; margin-bottom: 17px; }
  .copy p { font-size: 15px; line-height: 21px; letter-spacing: 0.5px; margin-bottom: 21px; }
  .copy strong { font-weight: 700; }

  .info-band { position: absolute; left: 40px; top: 880px; width: 753px; height: 183px; background: var(--slate); color: var(--white); display: flex; }
  .info-block { flex: 1; text-align: center; padding-top: 20px; }
  .info-title { font-size: 15px; font-weight: 700; letter-spacing: 1.3px; }
  .info-text { font-size: 15px; font-weight: 400; letter-spacing: 1.2px; line-height: 21px; margin-top: 22px; }

  .contact-bar { position: absolute; left: 40px; top: 1063px; width: 377px; height: 75px; background: var(--sky); color: var(--slate); }
  .web-bar { position: absolute; left: 417px; top: 1063px; width: 376px; height: 75px; background: var(--brand-blue); color: var(--white); }
  .bar-text { font-size: 15px; font-weight: 700; letter-spacing: 1.2px; line-height: 75px; }
  .contact-bar .bar-text { padding-left: 26px; }
  .web-bar .bar-text { padding-left: 63px; }
</style>
</head>
<body>
<main class="flyer">
  <div class="panel-gallery"></div>

  <div class="product-shot shot-seat" role="img" aria-label="Photo of seat with backrest and armrests, timber-look battens on a light aluminium frame"></div>
  <div class="product-shot shot-table" role="img" aria-label="Photo of table with dark composite battens on aluminium frame"></div>
  <div class="product-shot shot-setting" role="img" aria-label="Photo of table with two bench seats"></div>
  <div class="product-shot shot-bench" role="img" aria-label="Photo of seat with backrest, front view"></div>

  <header class="brand">
    <div class="brand-name">AVENUE</div>
    <div class="brand-line">Commons</div>
  </header>

  <section class="panel-copy copy">
    <h1 class="lead">European inspired with a unique and original design, that is functional all while respecting the environment.</h1>
    <p>Our range is designed to make life easier for people; created using extremely durable, ultra low maintenance materials.</p>
    <p>Featuring <strong>98% recycled</strong> composite battens in a range of stain and fade-resistant colour options and a unique aluminium frame design.</p>
    <p>The capped composite battens come with a <strong>10-year commercial warranty</strong> covering staining, fading and structural performance.</p>
    <p>Site-specific for healthcare applications offering wheelchair accessibility options</p>
    <p>The Avenue Commons range comprises of a seat with optional armrests, bench seat and table, available in both standard or DDA designs.</p>
    <p>Uniform length of 1800mm with tailored options available.</p>
    <p>Bolt down or freestanding options.</p>
  </section>

  <section class="info-band">
    <div class="info-block">
      <h2 class="info-title">RECYCLED CONTENT INFORMATION</h2>
      <p class="info-text">TEXT TO BE SUPPLIED -COULD<br>INCLUDE CUSTOM&nbsp; RECYCLE ICON</p>
    </div>
    <div class="info-block">
      <h2 class="info-title">10 YEAR WARRANTY INFORMATION</h2>
      <p class="info-text">TEXT TO BE SUPPLIED -COULD<br>INCLUDE WARRANTY ICON</p>
    </div>
  </section>

  <footer>
    <div class="contact-bar"><p class="bar-text">CONTACT INFORMATION GOES HERE</p></div>
    <div class="web-bar"><p class="bar-text">WEBSITE URL GOES HERE</p></div>
  </footer>
</main>
</body>
</html>
```